UK Supplement Company Needs a Label for Diet Protein Powder

We need a new, modern and fresh design for our Diet Protein Powder. Our protein powder is packaged in black plastic tubs (photo attached) and needs an attractive label. We would like to see designs that grab attention and look professional. We're very open to ideas. The label should be 88mm x 365mm. We also prefer PSD format where possible. These alterations could be made once your design is chosen. Have attached photo of our shake ingredients/benefits.

Target Market(s)

Slimmers

Industry/Entity Type

Health And Wellness

Font styles to use
Serif
Sans Serif

Colors

Designer to choose colors to be used in the design.

Requirements
Must have
• Clean, Modern and Professional Look. Eye catching. The flavour, we offer 6 flavours so this must be something we can edit (Flavours are Banana, Chocolate, Chocolate Mint, Strawberry, Toffee and Vanilla).
Nice to have
• Our logo, this can be Varlo Nutrition or just VARLO. Our logo files are attached.
Should not have
• We do not want to see people (faces or bodies) on the design.

```html
<!DOCTYPE html>
<html lang="en">
<head>
<meta charset="utf-8">
<title>VARLO Nutrition – Low Calorie Protein Shake Banana</title>
<link href="https://fonts.googleapis.com/css2?family=Tenor+Sans&family=Montserrat:wght@600&display=swap" rel="stylesheet">
<style>
  :root {
    --bg: #ecebea;
    --pouch: #2b2b2c;
    --pouch-edge: #1c1c1d;
    --lime: #b8e830;
    --label-pale: #e4e4dc;
    --label-yellow: #e2e45a;
    --label-green: #aee62e;
    --magenta: #c21fcb;
    --logo-bg: #2a2829;
    --white: #ffffff;
  }
  * { margin: 0; padding: 0; box-sizing: border-box; }
  html, body { width: 1193px; height: 1200px; overflow: hidden; }
  body { background: var(--bg); position: relative; font-family: "Tenor Sans", sans-serif; }

  .pouch {
    position: absolute; left: 276px; top: 60px; width: 640px; height: 1080px;
    background: linear-gradient(180deg, var(--pouch) 0%, #323233 50%, var(--pouch-edge) 100%);
    border-radius: 6px;
  }
  .pouch__seal {
    position: absolute; left: 0; right: 0; top: 0; height: 34px;
    border-bottom: 2px solid #3b3b3c;
  }
  .pouch__banana-band {
    position: absolute; left: 20px; right: 20px; top: 44px; height: 250px;
    background: radial-gradient(ellipse at 30% 40%, rgba(184,232,48,0.18), transparent 60%),
                radial-gradient(ellipse at 75% 70%, rgba(184,232,48,0.16), transparent 55%);
    border-radius: 4px;
  }
  .label {
    position: absolute; left: 70px; top: 320px; width: 500px; height: 610px;
    background: linear-gradient(100deg, var(--label-pale) 0%, var(--label-yellow) 50%, var(--label-green) 100%);
    text-align: center;
  }
  .logo {
    position: absolute; left: 185px; top: 80px; width: 130px; height: 130px;
    background: var(--logo-bg);
    display: flex; align-items: center; justify-content: center;
    font-family: "Montserrat", sans-serif; font-weight: 600;
    color: var(--white); font-size: 28px; letter-spacing: 1px;
  }
  .label__type {
    position: absolute; left: 0; right: 0; top: 232px;
    color: var(--magenta); font-size: 22px; letter-spacing: 1px;
  }
  .label__illustration {
    position: absolute; left: 165px; top: 280px; width: 170px; height: 170px;
    background: radial-gradient(ellipse at center, #f0d860 0%, #e8da5a 55%, rgba(232,218,90,0) 75%);
    border-radius: 50%;
  }
  .label__product {
    position: absolute; left: 0; right: 0; top: 470px;
    color: var(--magenta); font-size: 25px; font-weight: 400; letter-spacing: 1px; line-height: 1.3;
  }
  .pouch__icon-band {
    position: absolute; left: 20px; right: 20px; bottom: 24px; height: 100px;
    background: linear-gradient(90deg, rgba(184,232,48,0.22), rgba(184,232,48,0.32), rgba(184,232,48,0.22));
    border-radius: 4px;
  }
</style>
</head>
<body>
  <div class="pouch">
    <div class="pouch__seal"></div>
    <div class="pouch__banana-band" role="img" aria-label="Lime line drawings of banana bunches scattered across the top of the pouch"></div>

    <section class="label">
      <div class="logo">VARLO</div>
      <p class="label__type">DIETERY SYPPLEMENT</p>
      <div class="label__illustration" role="img" aria-label="Illustration of a yellow banana bunch"></div>
      <h1 class="label__product">LOW CALORIE PROTEIN SHAK<br>BANANA FLAVOUR</h1>
    </section>

    <div class="pouch__icon-band" role="img" aria-label="Pattern of lime outline fitness icons: dumbbells, trainers, kettlebells, balls and stars"></div>
  </div>
</body>
</html>
```